I am a surgeon that operates on gynaecological cancer. Wish a design and logo for letter head.

Design should include my name: Dr. Kiran Mudaly, qualifications: FTELSWOB, CGO. and state that I am a Gynaecological Oncologist and Advanced Laparoscopic Surgeon.
As for a logo. As all cancer is related to DNA, I think that that double helix could be used to symbolise a female shape, exaggerating the abdomen to suggest a mass.

Reason: Extended to view changes I have asked for.

```html
<!DOCTYPE html>
<html lang="en">
<head>
<meta charset="utf-8">
<title>Dr. Kiran Mudaly – Letterhead and Identity</title>
<link rel="stylesheet" href="https://fonts.googleapis.com/css2?family=Tinos:wght@700&family=Arimo:wght@400&display=swap">
<style>
  :root {
    --brand-blue: #336699;
    --brand-grey: #9a9a9a;
    --band-grey: #b3b3b3;
    --backdrop: #e6e6e6;
    --paper: #ffffff;
  }
  html, body { margin: 0; padding: 0; overflow: hidden; }
  .canvas {
    position: relative;
    width: 1200px;
    height: 1000px;
    background: var(--paper);
    overflow: hidden;
    font-family: "Arimo", Arial, sans-serif;
  }
  .backdrop {
    position: absolute; left: 0; top: 0;
    width: 737px; height: 1000px;
    background: var(--backdrop);
  }
  .shapes { position: absolute; left: 0; top: 0; }
  .name {
    position: absolute;
    margin: 0;
    font-family: "Tinos", "Times New Roman", serif;
    font-weight: 700;
    color: var(--brand-blue);
    white-space: nowrap;
    line-height: 1;
  }
  .credentials {
    position: absolute;
    margin: 0;
    color: var(--brand-grey);
    white-space: nowrap;
    line-height: 1;
  }
  .specialty {
    position: absolute;
    right: 524px; top: 121px;
    margin: 0;
    color: #ffffff;
    font-size: 11px;
    line-height: 18px;
    text-align: right;
  }
  .letter-name { left: 88px; top: 95px; font-size: 23px; }
  .letter-creds { left: 88px; top: 123px; font-size: 13px; letter-spacing: 7px; }
  .stacked-name { left: 788px; width: 400px; text-align: center; top: 202px; font-size: 32px; }
  .stacked-creds { left: 830px; top: 238px; font-size: 17px; letter-spacing: 11.5px; }
  .inline-name { left: 905px; top: 414px; font-size: 27px; }
  .inline-creds { left: 905px; top: 444px; font-size: 14px; letter-spacing: 8.2px; }

  .mark-name {
    position: absolute;
    margin: 0;
    font-family: "Tinos", "Times New Roman", serif;
    font-weight: 700;
    color: var(--brand-blue);
    text-align: center;
    line-height: 1.05;
  }
  .mark-letter  { left: 329px; top: 86px;  width: 88px;  font-size: 15px; }
  .mark-stacked { left: 928px; top: 98px;  width: 120px; font-size: 20px; }
  .mark-inline  { left: 799px; top: 421px; width: 88px;  font-size: 15px; }
  .mark-large   { left: 803px; top: 690px; width: 370px; font-size: 56px; }
</style>
</head>
<body>
<main class="canvas">
  <div class="backdrop"></div>

  <svg class="shapes" width="1200" height="1000" viewBox="0 0 1200 1000" aria-hidden="true">
    <rect class="sheet" x="53" y="55" width="630" height="890" fill="var(--paper)"/>
    <path class="header-band" d="M410 55 C442 82 440 140 385 160 L683 160 L683 55 Z" fill="var(--band-grey)"/>
    <ellipse cx="373" cy="103" rx="44" ry="42" fill="none" stroke="var(--brand-blue)" stroke-width="3"/>
    <ellipse cx="988" cy="118" rx="60" ry="58" fill="none" stroke="var(--brand-blue)" stroke-width="4"/>
    <ellipse cx="843" cy="440" rx="44" ry="42" fill="none" stroke="var(--brand-blue)" stroke-width="3"/>
    <ellipse cx="988" cy="752" rx="185" ry="170" fill="none" stroke="var(--brand-blue)" stroke-width="6"/>
    <line class="footer-rule" x1="88" y1="884" x2="649" y2="884" stroke="var(--brand-blue)" stroke-width="3"/>
  </svg>

  <!-- letterhead -->
  <h1 class="name letter-name">DR. KIRAN MUDALY</h1>
  <p class="credentials letter-creds">FTELSWOB, CGO.</p>
  <p class="mark-name mark-letter">Kiran<br>Mudaly</p>
  <p class="specialty">Gynaecological Oncologist<br>and Advanced Laparoscopic Surgeon.</p>

  <!-- stacked lockup -->
  <p class="mark-name mark-stacked">Kiran<br>Mudaly</p>
  <p class="name stacked-name">DR. KIRAN MUDALY</p>
  <p class="credentials stacked-creds">FTELSWOB, CGO.</p>

  <!-- inline lockup -->
  <p class="mark-name mark-inline">Kiran<br>Mudaly</p>
  <p class="name inline-name">DR. KIRAN MUDALY</p>
  <p class="credentials inline-creds">FTELSWOB, CGO.</p>

  <!-- large mark -->
  <p class="mark-name mark-large">Kiran<br>Mudaly</p>
</main>
</body>
</html>
```